Business is called "Kestrel Ledger". Accounting and tax services.

I need a flyer for my new business "Kestrel Ledger". I am an individual accountant working for himself on the Sunshine Coast in Queensland Australia. I would like to see designs that communicate reliability and trust. I believe my point of difference is that I am always available to my clients and I will cap my number of clients to ensure I can service them properly. Accountants in general seem to have a bad reputation for not responding to clients in a timely fashion, whether by email or phone. This is where I intend to differentiate myself. I have included my business card for ideas on colour and for contact information. I have also included some logo's that should go on the flyer. With the QLA logo, the words "Kestrel Ledger is a QLA Business" needs to be written either above, below or to the right hand side (as per the business card).

Target Market(s)

Small business owners and individuals requiring taxation and financials

Industry/Entity Type

Public Accounting

Font styles to use
Serif

Requirements
Must have
• Supplied logo's, accounting style pictures etc
Services: Small Business Taxation
Company & Trust Tax Returns
Rental Property Returns
Capital Gains Tax
Individual Tax Returns
BAS and IAS lodgements
Nice to have
• Needs to convey a sense of being reliable and responds to clients quickly.
Should not have
• My name

```html
<!DOCTYPE html>
<html lang="en">
<head>
<meta charset="utf-8">
<title>Kestrel Ledger – Accounting &amp; Tax Flyer</title>
<link rel="stylesheet" href="https://fonts.googleapis.com/css2?family=Playfair+Display:wght@700;800&family=Lora:ital,wght@0,400;0,500;0,700;1,400&display=swap">
<style>
  :root {
    --mint-glass: rgba(86, 200, 172, 0.93);
    --teal: #27a88a;
    --teal-deep: #1f9c80;
    --ink: #2e2e2e;
    --muted: #8a8a8a;
    --paper: #ffffff;
    --rule: #b9b9b9;
  }
  * { box-sizing: border-box; margin: 0; padding: 0; }
  html, body { width: 855px; height: 1200px; overflow: hidden; background: var(--paper); }
  .flyer {
    position: relative;
    width: 855px; height: 1200px;
    background: var(--paper);
    font-family: "Lora", serif;
    color: var(--ink);
  }
  .hero-photo {
    position: absolute; left: 0; top: 100px; width: 707px; height: 568px;
    background:
      linear-gradient(100deg, rgba(20,28,36,0.92) 0%, rgba(30,40,50,0.75) 32%, rgba(60,72,84,0.35) 52%, rgba(30,38,48,0.8) 72%, rgba(24,30,38,0.9) 100%),
      linear-gradient(180deg, #dfe5ea 0%, #c6ced6 45%, #3a434c 80%, #1b2128 100%);
  }
  .headline-panel {
    position: absolute; left: 421px; top: 0; width: 434px; height: 350px;
    background: var(--mint-glass);
  }
  .headline {
    position: absolute; left: 51px; top: 64px;
    font-family: "Playfair Display", serif;
    font-weight: 800; text-transform: uppercase;
    font-size: 31px; line-height: 54px; letter-spacing: 0.3px;
    color: var(--paper);
  }
  .headline-arrow { position: absolute; left: 307px; top: 198px; }
  .contact-band {
    position: absolute; left: 181px; top: 608px; width: 526px; height: 60px;
    background: var(--teal);
    display: flex; align-items: center; justify-content: center; gap: 20px;
    color: var(--paper); font-size: 17px; font-weight: 500;
  }
  .services-title {
    position: absolute; left: 328px; top: 737px; width: 199px; height: 45px;
    background: var(--teal-deep);
    color: var(--paper); font-family: "Playfair Display", serif; font-weight: 700; font-size: 20px;
    display: flex; align-items: center; justify-content: center; letter-spacing: 0.5px;
  }
  .service {
    position: absolute; width: 220px;
    font-weight: 700; font-size: 15px; line-height: 20px; text-transform: uppercase;
  }
  .service::after {
    content: ""; display: block; width: 59px; height: 5px;
    background: var(--teal); margin-top: 14px;
  }
  .promise {
    position: absolute; left: 0; top: 1022px; width: 855px; text-align: center;
    font-style: italic; font-size: 15px; color: var(--teal-deep);
  }
  .brand {
    position: absolute; left: 20px; top: 1082px; width: 180px;
    display: flex; flex-direction: column; align-items: center; gap: 12px;
  }
  .brand-mark { width: 46px; height: 46px; border: 2px solid var(--ink); border-radius: 50%; }
  .brand-name { font-size: 12px; font-weight: 500; letter-spacing: 2.5px; color: var(--ink); white-space: nowrap; }
  .footer-rule { position: absolute; left: 217px; top: 1093px; width: 3px; height: 47px; background: var(--rule); }
  .partner-square { position: absolute; left: 256px; top: 1100px; width: 58px; height: 25px; background: #1c4f9c; }
  .partner-badge { position: absolute; left: 354px; top: 1093px; width: 38px; height: 38px; border-radius: 50%; background: #e9d94a; border: 3px solid #fff; box-shadow: 0 0 0 1px #c9c9c9; }
  .partner-circle { position: absolute; left: 435px; top: 1092px; width: 41px; height: 41px; border-radius: 50%; background: #1ab4e8; }
  .qla-note {
    position: absolute; left: 256px; top: 1146px;
    font-size: 11px; color: var(--muted); white-space: nowrap;
  }
  .footer-contact {
    position: absolute; right: 48px; top: 1118px; text-align: right;
    font-size: 15px; line-height: 19px; color: var(--muted); font-style: normal;
  }
</style>
</head>
<body>
<main class="flyer">
  <div class="hero-photo" role="img" aria-label="Upward view of dark glass office towers against a pale cloudy sky"></div>

  <section class="headline-panel">
    <h1 class="headline">We do the numbers<br>and help your<br>business<br>grow</h1>
    <svg class="headline-arrow" width="66" height="76" viewBox="0 0 66 76" aria-hidden="true">
      <polyline points="4,4 60,38 4,72" fill="none" stroke="#ffffff" stroke-width="6" stroke-linejoin="miter"/>
    </svg>
  </section>

  <div class="contact-band">
    <span>Call: 0755 012 345</span><span>|</span><span>support@kestrelledger.com.au</span>
  </div>

  <h2 class="services-title">OUR SERVICES</h2>

  <p class="service" style="left:80px; top:822px;">Small business<br>taxation</p>
  <p class="service" style="left:333px; top:822px;">Company &amp; trust<br>tax returns</p>
  <p class="service" style="left:605px; top:822px;">Rental property<br>returns</p>
  <p class="service" style="left:80px; top:931px;">Capital gains<br>tax</p>
  <p class="service" style="left:333px; top:931px;">Individual tax<br>returns</p>
  <p class="service" style="left:605px; top:931px;">BAS and IAS<br>lodgements</p>

  <p class="promise">Always available, always quick to reply – client numbers are capped so every client gets proper service.</p>

  <footer>
    <div class="brand">
      <span class="brand-mark"></span>
      <span class="brand-name">KESTREL LEDGER</span>
    </div>
    <span class="footer-rule"></span>
    <span class="partner-square" role="img" aria-label="QLA membership badge"></span>
    <span class="partner-badge" role="img" aria-label="Registered tax agent badge"></span>
    <span class="partner-circle" role="img" aria-label="Accounting software partner badge"></span>
    <p class="qla-note">Kestrel Ledger is a QLA Business</p>
    <address class="footer-contact">
      0755 012 345<br>support@kestrelledger.com.au
    </address>
  </footer>
</main>
</body>
</html>
```